Brightmoor Learning Data Dashboard

Brightmoor Learning is a leading provider of digital curriculum and online courses to increase educational opportunities and achievement to students in grades K-12. Teachers and students access all course materials online.

School districts need greater visibility into the rate in which students are progressing through their courses, so school staff can better support students to complete courses at the required rate to keep them on track for graduation.
This can be accomplished by allowing school administrators to view a data dashboard and pull an on-demand report and see progress for a specified date range, relative to overall progress.

Within a specified date range, school administrators want to know if the student made more or less progress than in the period prior to the first date in the range.
School administrators also want to know if students are ahead or behind where they should be after the second date in the range.

Industry/Entity Type

Digital

```html
<!DOCTYPE html>
<html lang="en">
<head>
<meta charset="utf-8">
<title>Time Based Performance Report – Brightmoor Learning</title>
<link href="https://fonts.googleapis.com/css2?family=Lato:wght@400;700;900&display=swap" rel="stylesheet">
<style>
:root{
  --navy:#2b2654;
  --page:#ecebf5;
  --white:#ffffff;
  --ink:#333333;
  --icon:#6b6b6b;
  --rule:#c9c9d3;
  --clear:#bdbdc7;
  --green-btn:#2f8f1f;
  --bad:#ff0000;
  --good:#1aa23a;
  --cell-line:#9a9a9a;
}
*{box-sizing:border-box;margin:0;padding:0}
html,body{width:1200px;height:1081px;overflow:hidden;background:var(--page)}
body{font-family:'Lato',sans-serif;color:var(--ink)}
.stage{width:1400px;height:1261px;transform:scale(.857143);transform-origin:0 0;position:relative;background:var(--page)}
.topbar{position:absolute;left:0;top:0;width:1400px;height:113px;background:var(--white);border-bottom:1px solid var(--rule)}
.brand{position:absolute;left:38px;top:40px;display:flex;align-items:center;gap:10px;font-weight:700;font-size:19px;color:var(--navy);letter-spacing:.5px;line-height:1.05}
.brand-dot{width:30px;height:30px;border-radius:50%;background:var(--navy)}
.tools{position:absolute;top:20px;right:115px;display:flex;align-items:center;gap:26px}
.tools svg{display:block}
.mail{position:relative}
.badge{position:absolute;right:-8px;top:-8px;width:17px;height:17px;border-radius:50%;background:var(--navy);color:#fff;font-size:11px;font-weight:700;text-align:center;line-height:17px}
.avatar{width:74px;height:74px;border-radius:50%;border:3px solid #e4e4e4;background:radial-gradient(circle at 50% 40%,#c9a58f,#6b5a52);margin-left:30px}
.navbar{position:absolute;left:0;top:114px;width:1400px;height:51px;background:var(--white);border-bottom:1px solid var(--rule);display:flex;padding-left:124px;gap:0}
.nav-item{display:flex;align-items:center;gap:10px;font-size:17px;font-weight:700;color:#3a3a3a;margin-right:58px}
.nav-item svg{fill:var(--icon)}
h1{position:absolute;top:228px;left:0;width:1400px;text-align:center;font-size:36px;font-weight:900;color:var(--navy)}
.filters label{position:absolute;top:325px;font-size:17px;color:#333}
.radio{display:inline-block;width:14px;height:14px;border-radius:50%;vertical-align:-1px;margin-right:6px}
.radio.on{background:var(--navy)}
.radio.off{border:2px solid #555}
.field{position:absolute;top:364px;width:282px;height:48px;background:var(--white);border:1px solid #cfcfd6;font-size:16px;color:#555;padding-left:17px;line-height:46px}
.field .clear{position:absolute;right:0;top:0;width:51px;height:46px;background:var(--clear);display:flex;align-items:center;justify-content:center}
.download{position:absolute;left:573px;top:456px;width:255px;height:65px;border-radius:33px;background:var(--green-btn);color:#fff;font-size:20px;font-weight:700;display:flex;align-items:center;justify-content:center;gap:10px;letter-spacing:.3px}
.report{position:absolute;left:115px;top:587px;width:1170px;border-collapse:collapse;table-layout:fixed;font-size:14px}
.report th{background:var(--navy);color:#fff;font-weight:400;font-size:15px;line-height:20px;border:1px solid #5a5580;text-align:center;vertical-align:middle;padding:0}
.report th.small{font-size:12px}
.report td{background:var(--white);height:60px;border:1px solid var(--cell-line);text-align:center;vertical-align:middle;color:#333;padding:0}
.report td.bad{background:var(--bad);color:#fff}
.report td.good{background:var(--good);color:#fff}
.footer-rule{position:absolute;left:115px;top:1159px;width:1170px;border-top:1px solid #9a9a9a}
.copyright{position:absolute;top:1199px;left:0;width:1400px;text-align:center;font-size:15px;color:#444}
</style>
</head>
<body>
<div class="stage">
  <header class="topbar">
    <div class="brand"><span class="brand-dot"></span><span>BRIGHTMOOR LEARNING</span></div>
    <div class="tools">
      <svg width="24" height="24" viewBox="0 0 24 24" aria-label="Settings"><path fill="#6b6b6b" d="M10 1h4l.6 3 2.2 1 2.6-1.7 2.8 2.8-1.7 2.6 1 2.2 3 .6v4l-3 .6-1 2.2 1.7 2.6-2.8 2.8-2.6-1.7-2.2 1-.6 3h-4l-.6-3-2.2-1-2.6 1.7-2.8-2.8 1.7-2.6-1-2.2-3-.6v-4l3-.6 1-2.2L1.8 5.8l2.8-2.8L7.2 4.7l2.2-1zM12 8a4 4 0 100 8 4 4 0 000-8z"/></svg>
      <svg width="26" height="28" viewBox="0 0 26 28" aria-label="Notifications"><path fill="none" stroke="#6b6b6b" stroke-width="2" d="M5 20V12a8 8 0 0116 0v8l2 3H3zM10 25a3 3 0 006 0"/></svg>
      <div class="mail"><svg width="28" height="22" viewBox="0 0 28 22" aria-label="Messages"><rect x="1" y="1" width="26" height="20" rx="2" fill="none" stroke="#6b6b6b" stroke-width="2"/><path d="M1 2l13 10 13-10" fill="none" stroke="#6b6b6b" stroke-width="2"/></svg><span class="badge">0</span></div>
      <div class="avatar" role="img" aria-label="User profile photo"></div>
      <svg width="12" height="8" viewBox="0 0 12 8"><path d="M0 0h12L6 7z" fill="#6b6b6b"/></svg>
    </div>
  </header>

  <nav class="navbar">
    <div class="nav-item"><svg width="28" height="22" viewBox="0 0 28 22"><path d="M14 2A13 13 0 001 15v5h26v-5A13 13 0 0014 2zm1 15a2 2 0 11-2-2l4-7 1 1-3 6z"/></svg>DASHBOARD</div>
    <div class="nav-item"><svg width="24" height="24" viewBox="0 0 24 24"><path d="M12 1a11 11 0 100 22 11 11 0 000-22zm-1.5 5h3v3h-3zm0 5h3v7h-3z"/></svg>RECENT</div>
    <div class="nav-item"><svg width="26" height="24" viewBox="0 0 26 24"><rect x="0" y="0" width="11" height="10" rx="1"/><rect x="14" y="0" width="11" height="10" rx="1"/><rect x="0" y="13" width="11" height="10" rx="1"/><rect x="14" y="13" width="11" height="10" rx="1"/></svg>APPS</div>
    <div class="nav-item"><svg width="28" height="24" viewBox="0 0 28 24"><path d="M17 0l11 9-11 9v-5C9 13 4 16 1 23 2 12 8 6 17 5z"/></svg>SHARED WITH ME</div>
    <div class="nav-item"><svg width="28" height="26" viewBox="0 0 28 26"><path fill="none" stroke="#6b6b6b" stroke-width="2" d="M9 7V1h10l6 6v12h-8M1 7h10l6 6v12H1z"/></svg>PAGES</div>
    <div class="nav-item"><svg width="30" height="26" viewBox="0 0 30 26"><circle cx="7" cy="6" r="4"/><circle cx="23" cy="6" r="4"/><circle cx="15" cy="9" r="5"/><path d="M0 19a7 6 0 0114 0v2H0zM16 19a7 6 0 0114 0v2H16zM5 24a10 8 0 0120 0v2H5z"/></svg>MANAGEMENT</div>
  </nav>

  <h1>Time Based Performance Report</h1>

  <section class="filters">
    <label style="left:113px">School:</label>
    <label style="left:410px"><span class="radio on"></span>Observer:</label>
    <label style="left:528px"><span class="radio off"></span>Teacher:</label>
    <label style="left:706px">Filter Date 1:</label>
    <label style="left:1002px">Filter Date 2:</label>
    <div class="field" style="left:114px">Choose a school..<span class="clear"><svg width="16" height="16" viewBox="0 0 16 16"><circle cx="8" cy="8" r="7" fill="#fff"/><path d="M5.5 5.5l5 5M10.5 5.5l-5 5" stroke="#bdbdc7" stroke-width="2"/></svg></span></div>
    <div class="field" style="left:411px">Choose an observer...<span class="clear"><svg width="16" height="16" viewBox="0 0 16 16"><circle cx="8" cy="8" r="7" fill="#fff"/><path d="M5.5 5.5l5 5M10.5 5.5l-5 5" stroke="#bdbdc7" stroke-width="2"/></svg></span></div>
    <div class="field" style="left:707px">2/27/18<span class="clear"><svg width="16" height="16" viewBox="0 0 16 16"><circle cx="8" cy="8" r="7" fill="#fff"/><path d="M5.5 5.5l5 5M10.5 5.5l-5 5" stroke="#bdbdc7" stroke-width="2"/></svg></span></div>
    <div class="field" style="left:1003px">2/6/18<span class="clear"><svg width="16" height="16" viewBox="0 0 16 16"><circle cx="8" cy="8" r="7" fill="#fff"/><path d="M5.5 5.5l5 5M10.5 5.5l-5 5" stroke="#bdbdc7" stroke-width="2"/></svg></span></div>
  </section>

  <div class="download"><svg width="18" height="18" viewBox="0 0 18 18"><path d="M7 0h4v7h4l-6 6-6-6h4zM0 14h3v2h12v-2h3v4H0z" fill="#fff"/></svg>DOWNLOAD EXCEL</div>

  <table class="report">
    <colgroup>
      <col style="width:92px"><col style="width:82px"><col style="width:82px"><col style="width:82px"><col style="width:62px"><col style="width:62px"><col style="width:62px"><col style="width:62px"><col style="width:59px"><col style="width:60px"><col style="width:58px"><col style="width:59px"><col style="width:69px"><col style="width:61px"><col style="width:79px"><col style="width:79px"><col style="width:60px">
    </colgroup>
    <thead>
      <tr style="height:32px">
        <th rowspan="3">Student<br>Name</th><th rowspan="3">Observer</th><th rowspan="3">School</th><th rowspan="3">Course<br>Title</th><th rowspan="3">Current<br>Grade</th><th rowspan="3">Raw<br>Score</th><th rowspan="3">Course<br>Start<br>Date</th><th rowspan="3">Course<br>End<br>Date</th>
        <th colspan="4">Percent Complete</th>
        <th rowspan="3">2/27-3/6<br>progress<br>Actual/<br>Goal</th><th rowspan="3">Status<br>as of<br>march 6</th><th rowspan="3">Completion<br>Rate/day<br>fot the<br>range</th><th rowspan="3">Completion<br>Rate<br>Change</th><th rowspan="3">Last<br>Login</th>
      </tr>
      <tr style="height:33px"><th colspan="2">Start 2/27/18</th><th colspan="2">End 2/6/18</th></tr>
      <tr style="height:28px"><th class="small">Actual %</th><th class="small">Goal %</th><th class="small">Actual %</th><th class="small">Goal %</th></tr>
    </thead>
    <tbody>
      <tr><td>Elliot</td><td>Lia Moss</td><td>Linwood</td><td>Biology</td><td>67.3%</td><td>70%</td><td>2/10/18</td><td>4/24/18</td><td>0%</td><td>10%</td><td>5%</td><td>20%</td><td class="bad">5/10</td><td class="bad">5/20</td><td>.2%</td><td><svg width="12" height="26" viewBox="0 0 12 26"><path d="M6 0l6 8H8v18H4V8H0z" fill="#333"/></svg></td><td>3/6/18</td></tr>
      <tr><td>Elliot</td><td>Lia Moss</td><td>Linwood</td><td>Biology</td><td>67.3%</td><td>70%</td><td>2/10/18</td><td>4/24/18</td><td>0%</td><td>10%</td><td>5%</td><td>20%</td><td class="good">5/10</td><td class="bad">5/20</td><td>.2%</td><td><svg width="12" height="26" viewBox="0 0 12 26"><path d="M6 0l6 8H8v18H4V8H0z" fill="#333"/></svg></td><td>3/6/18</td></tr>
      <tr><td>Elliot</td><td>Lia Moss</td><td>Linwood</td><td>Biology</td><td>67.3%</td><td>70%</td><td>2/10/18</td><td>4/24/18</td><td>0%</td><td>10%</td><td>5%</td><td>20%</td><td class="bad">5/10</td><td class="good">5/20</td><td>.2%</td><td><svg width="12" height="26" viewBox="0 0 12 26"><path d="M6 26l6-8H8V0H4v18H0z" fill="#333"/></svg></td><td>3/6/18</td></tr>
      <tr><td>Elliot</td><td>Lia Moss</td><td>Linwood</td><td>Biology</td><td>67.3%</td><td>70%</td><td>2/10/18</td><td>4/24/18</td><td>0%</td><td>10%</td><td>5%</td><td>20%</td><td class="bad">5/10</td><td class="bad">5/20</td><td>.2%</td><td><svg width="12" height="26" viewBox="0 0 12 26"><path d="M6 26l6-8H8V0H4v18H0z" fill="#333"/></svg></td><td>3/6/18</td></tr>
      <tr><td>Elliot</td><td>Lia Moss</td><td>Linwood</td><td>Biology</td><td>67.3%</td><td>70%</td><td>2/10/18</td><td>4/24/18</td><td>0%</td><td>10%</td><td>5%</td><td>20%</td><td class="good">5/10</td><td class="good">5/20</td><td>.2%</td><td><svg width="12" height="26" viewBox="0 0 12 26"><path d="M6 0l6 8H8v18H4V8H0z" fill="#333"/></svg></td><td>3/6/18</td></tr>
      <tr><td>Elliot</td><td>Lia Moss</td><td>Linwood</td><td>Biology</td><td>67.3%</td><td>70%</td><td>2/10/18</td><td>4/24/18</td><td>0%</td><td>10%</td><td>5%</td><td>20%</td><td class="bad">5/10</td><td class="bad">5/20</td><td>.2%</td><td><svg width="28" height="12" viewBox="0 0 28 12"><path d="M0 6l7-6v4h14V0l7 6-7 6V8H7v4z" fill="#333"/></svg></td><td>3/6/18</td></tr>
      <tr><td>Elliot</td><td>Lia Moss</td><td>Linwood</td><td>Biology</td><td>67.3%</td><td>70%</td><td>2/10/18</td><td>4/24/18</td><td>0%</td><td>10%</td><td>5%</td><td>20%</td><td class="good">5/10</td><td class="good">5/20</td><td>.2%</td><td><svg width="28" height="12" viewBox="0 0 28 12"><path d="M0 6l7-6v4h14V0l7 6-7 6V8H7v4z" fill="#333"/></svg></td><td>3/6/18</td></tr>
    </tbody>
  </table>

  <div class="footer-rule"></div>
  <p class="copyright">© 2018, Brightmoor Learning. All Rights Reserved.</p>
</div>
</body>
</html>
```